Brochure Projecct

I need a brochure created for my company, which will be sent to customers via email in PDF format. I have uploaded the company logo with this project, which I want incorporated in the design.

Designers should view the company website at www.brightcounselpages.com. I want the brochure to compliment the website (i.e., very clean design). I would also like pictures added to the brochure to make the design visually stunning.

In terms of content, I need four pages in the brochure to add four separate sections of content (one section per page). The four sections of content will be as follows (1) Search Engine Optimization Benefits (2) Increased Client Retention (3) Showcase Your Law Firm (4) Maximize Your Online ROI (5) Pricing Plans. I will give the content to the winning designer to add to the project. Each individual content section will have four subsection titles after which content of approximately 100 to 200 words will appear.

Designers can decide if other pages should be added to the brochure (i.e., a "cover page" that would have little content, but be visually appealing like the cover of a book - - - a "back page" that may just have the logo, contact information, etc).

My company address and email address should be prominently featured through every page (address: 2715 West Juniper Avenue, Suite 1400, Scottsdale, Arizona 85317; email: sales@brightcounselpages.com).

Industry/Entity Type

It Company

Requirements
Must have
• Clean look but visually stunning incorporating the design of the website at brightcounselpages.com as well as the logo. Also, room for content as set forth in the description of this project.

```html
<!DOCTYPE html>
<html lang="en">
<head>
<meta charset="utf-8">
<title>Bright Counsel Pages Brochure Presentation</title>
<link href="https://fonts.googleapis.com/css2?family=Arimo:ital,wght@0,400;0,700;1,400;1,700&display=swap" rel="stylesheet">
<style>
  :root {
    --sheet-bg: #ffffff;
    --heading-blue: #1f5fae;
    --page-deep: #0b4596;
    --page-mid: #1a63bb;
    --page-light: #3f8bd8;
    --band: #1a5fb3;
    --band-light: #4f98dc;
    --swoosh: rgba(110, 185, 240, 0.30);
    --swoosh-edge: rgba(150, 210, 250, 0.45);
    --text-white: #ffffff;
    --text-soft: #e6f0ff;
  }
  * { box-sizing: border-box; margin: 0; padding: 0; }
  html, body { width: 1200px; height: 900px; overflow: hidden; background: var(--sheet-bg); }
  body { font-family: "Arimo", Arial, sans-serif; position: relative; }

  .sheet-title {
    position: absolute; left: 33px; top: 24px;
    font-size: 16px; font-weight: 700; color: var(--heading-blue);
  }

  .page {
    position: absolute; width: 353px; height: 353px; overflow: hidden;
    background: linear-gradient(165deg, var(--page-mid) 0%, var(--page-deep) 50%, var(--page-mid) 100%);
    color: var(--text-white);
  }
  .page--r1 { top: 68px; }
  .page--r2 { top: 458px; }
  .page--c1 { left: 33px; }
  .page--c2 { left: 423px; }
  .page--c3 { left: 814px; }

  .page-art { position: absolute; inset: 0; width: 353px; height: 353px; }

  .page-band {
    position: absolute; left: 0; top: 0; width: 100%; height: 31px;
    background: linear-gradient(180deg, var(--band) 0%, var(--band-light) 100%);
  }
  .page-title {
    position: absolute; left: 17px; top: 15px;
    font-size: 12.5px; font-weight: 700; color: var(--text-white);
  }

  .column { position: absolute; top: 36px; font-size: 5.6px; line-height: 7px; color: var(--text-soft); }
  .column--left { left: 17px; width: 150px; }
  .column--right { left: 180px; width: 160px; }
  .column h3 { font-size: 7.2px; font-weight: 700; color: var(--text-white); line-height: 9px; margin-top: 2px; }
  .column p { margin-bottom: 3px; }

  .page-footer {
    position: absolute; left: 17px; bottom: 11px;
    font-size: 5.6px; font-style: italic; color: var(--text-soft); white-space: nowrap;
  }
  .page-footer b { color: var(--text-white); }

  .cover {
    background: radial-gradient(ellipse at 45% 30%, var(--page-light) 0%, var(--page-mid) 45%, var(--page-deep) 100%);
  }
  .brand { position: absolute; left: 20px; top: 105px; display: flex; align-items: center; gap: 12px; }
  .brand-mark { width: 56px; height: 56px; border-radius: 50%; background: var(--page-light); }
  .brand-name { font-size: 26px; font-weight: 700; color: var(--text-white); line-height: 27px; }
  .cover-tagline {
    position: absolute; left: 17px; top: 294px;
    font-size: 12.5px; font-weight: 700; color: var(--text-white);
  }
  .cover-contact {
    position: absolute; left: 17px; top: 314px;
    font-size: 7px; line-height: 9px; color: var(--text-soft);
  }
  .cover-contact b { color: var(--text-white); }
</style>
</head>
<body>

<h1 class="sheet-title">Local Law Firm Brochure Presentation</h1>

<section class="page page--r1 page--c1 cover">
  <svg class="page-art" viewBox="0 0 353 353">
    <path d="M0 250 C90 215 220 235 353 190 L353 353 L0 353 Z" fill="rgba(255,255,255,0.05)"/>
  </svg>
  <div class="brand">
    <span class="brand-mark"></span>
    <span class="brand-name">Bright Counsel<br>Pages</span>
  </div>
  <p class="cover-tagline">A local list of experienced Arizona lawyers</p>
  <p class="cover-contact">2715 West Juniper Avenue, Suite 1400, Scottsdale, Arizona 85317<br>sales@brightcounselpages.com &nbsp;<b>www.brightcounselpages.com</b></p>
</section>

<section class="page page--r1 page--c2">
  <svg class="page-art" viewBox="0 0 353 353">
    <defs>
      <radialGradient id="art-sky" cx="0.45" cy="0.35" r="0.8">
        <stop offset="0" stop-color="#eef5fb"/><stop offset="0.35" stop-color="#a9cbe8"/><stop offset="0.7" stop-color="#4f8fcc"/><stop offset="1" stop-color="#1f5ea8"/>
      </radialGradient>
    </defs>
    <path d="M110 353 C140 250 250 170 353 150 L353 353 Z" fill="var(--swoosh)"/>
    <path d="M110 353 C140 250 250 170 353 150" fill="none" stroke="var(--swoosh-edge)" stroke-width="2"/>
    <path role="img" aria-label="Photo of a bald eagle soaring over snowy mountains" fill="url(#art-sky)" d="M170 255 C170 212 228 192 283 194 C333 196 358 220 354 258 C350 288 337 300 320 306 L340 326 L298 310 C238 318 170 300 170 255 Z"/>
  </svg>
  <div class="page-band"></div>
  <h2 class="page-title">Search Engine Optimization Benefits</h2>
  <div class="column column--left">
    <h3>Sub Head</h3>
    <p>Every listing is written to be found by local clients searching for trusted legal help.</p>
    <p>Search engines reward pages that are clear, fast and useful. We build each firm profile with plain headings, accurate practice areas and local terms that match what people type, so your name appears where new clients begin their search for advice.</p>
    <p>Regular updates keep your profile fresh in the results. Our team reviews keywords, links and page speed each month, then reports the gains in simple terms so you always know how your listing performs against other firms nearby.</p>
    <h3>Sub Head</h3>
    <p>Strong local signals help your firm stand out in the map results for your city.</p>
    <p>We confirm your address, hours and phone details across trusted directories, so search engines see one consistent record. Matching details build trust, lift your ranking and make it simple for a client to call, visit or send a message.</p>
    <p>Reviews from past clients add weight to every profile. We show ratings clearly beside your practice areas, helping new visitors choose with confidence and giving search engines fresh content that keeps your page moving up the list.</p>
    <h3>Sub Head</h3>
    <p>Good content answers real questions. Short guides on divorce, injury, estate planning and business law bring steady visits, and each guide links back to your profile so readers can reach your office the moment they are ready.</p>
  </div>
  <div class="column column--right">
    <p>Mobile visitors now make up most searches for lawyers. Every page adapts to phones and tablets, with large buttons that let clients call your office in one tap.</p>
    <h3>Sub Head</h3>
    <p>Clear monthly reports show exactly where each new enquiry came from.</p>
    <p>You will see visits, calls and emails in one simple summary. We compare results over time and suggest small changes that bring better leads, so your budget is always spent on the pages and terms that work best for your firm.</p>
    <p>Our support team is on hand to answer questions, update details and add new attorneys or practice areas whenever your firm grows.</p>
  </div>
  <p class="page-footer">Address: <b>2715 West Juniper Avenue, Suite 1400, Scottsdale, Arizona 85317</b> &nbsp; Email: <b>sales@brightcounselpages.com</b></p>
</section>

<section class="page page--r1 page--c3">
  <svg class="page-art" viewBox="0 0 353 353">
    <defs>
      <radialGradient id="art-river" cx="0.5" cy="0.45" r="0.8">
        <stop offset="0" stop-color="#7a5f44"/><stop offset="0.45" stop-color="#4d5a52"/><stop offset="0.8" stop-color="#2e4e63"/><stop offset="1" stop-color="#1a3556"/>
      </radialGradient>
    </defs>
    <path d="M110 353 C140 250 250 170 353 150 L353 353 Z" fill="var(--swoosh)"/>
    <path d="M110 353 C140 250 250 170 353 150" fill="none" stroke="var(--swoosh-edge)" stroke-width="2"/>
    <path role="img" aria-label="Photo of a beaver swimming in a river" fill="url(#art-river)" d="M170 255 C170 212 228 192 283 194 C333 196 358 220 354 258 C350 288 337 300 320 306 L340 326 L298 310 C238 318 170 300 170 255 Z"/>
  </svg>
  <div class="page-band"></div>
  <h2 class="page-title">Increased Client Retention</h2>
  <div class="column column--left">
    <h3>Sub Head</h3>
    <p>Every listing is written to be found by local clients searching for trusted legal help.</p>
    <p>Search engines reward pages that are clear, fast and useful. We build each firm profile with plain headings, accurate practice areas and local terms that match what people type, so your name appears where new clients begin their search for advice.</p>
    <p>Regular updates keep your profile fresh in the results. Our team reviews keywords, links and page speed each month, then reports the gains in simple terms so you always know how your listing performs against other firms nearby.</p>
    <h3>Sub Head</h3>
    <p>Strong local signals help your firm stand out in the map results for your city.</p>
    <p>We confirm your address, hours and phone details across trusted directories, so search engines see one consistent record. Matching details build trust, lift your ranking and make it simple for a client to call, visit or send a message.</p>
    <p>Reviews from past clients add weight to every profile. We show ratings clearly beside your practice areas, helping new visitors choose with confidence and giving search engines fresh content that keeps your page moving up the list.</p>
    <h3>Sub Head</h3>
    <p>Good content answers real questions. Short guides on divorce, injury, estate planning and business law bring steady visits, and each guide links back to your profile so readers can reach your office the moment they are ready.</p>
  </div>
  <div class="column column--right">
    <p>Mobile visitors now make up most searches for lawyers. Every page adapts to phones and tablets, with large buttons that let clients call your office in one tap.</p>
    <h3>Sub Head</h3>
    <p>Clear monthly reports show exactly where each new enquiry came from.</p>
    <p>You will see visits, calls and emails in one simple summary. We compare results over time and suggest small changes that bring better leads, so your budget is always spent on the pages and terms that work best for your firm.</p>
    <p>Our support team is on hand to answer questions, update details and add new attorneys or practice areas whenever your firm grows.</p>
  </div>
  <p class="page-footer">Address: <b>2715 West Juniper Avenue, Suite 1400, Scottsdale, Arizona 85317</b> &nbsp; Email: <b>sales@brightcounselpages.com</b></p>
</section>

<section class="page page--r2 page--c1">
  <svg class="page-art" viewBox="0 0 353 353">
    <defs>
      <radialGradient id="art-aquarium" cx="0.55" cy="0.2" r="0.9">
        <stop offset="0" stop-color="#8fe0f5"/><stop offset="0.35" stop-color="#3bb0dc"/><stop offset="0.7" stop-color="#137db3"/><stop offset="1" stop-color="#053a66"/>
      </radialGradient>
    </defs>
    <path d="M110 353 C140 250 250 170 353 150 L353 353 Z" fill="var(--swoosh)"/>
    <path d="M110 353 C140 250 250 170 353 150" fill="none" stroke="var(--swoosh-edge)" stroke-width="2"/>
    <path role="img" aria-label="Photo of a large aquarium tank with a whale shark and fish" fill="url(#art-aquarium)" d="M170 250 C170 205 228 185 284 187 C334 189 360 214 356 254 C352 286 338 302 322 308 L340 330 L300 312 C240 322 170 302 170 250 Z"/>
  </svg>
  <div class="page-band"></div>
  <h2 class="page-title">Showcase Your Law Firm</h2>
  <div class="column column--left">
    <h3>Sub Head</h3>
    <p>Every listing is written to be found by local clients searching for trusted legal help.</p>
    <p>Search engines reward pages that are clear, fast and useful. We build each firm profile with plain headings, accurate practice areas and local terms that match what people type, so your name appears where new clients begin their search for advice.</p>
    <p>Regular updates keep your profile fresh in the results. Our team reviews keywords, links and page speed each month, then reports the gains in simple terms so you always know how your listing performs against other firms nearby.</p>
    <h3>Sub Head</h3>
    <p>Strong local signals help your firm stand out in the map results for your city.</p>
    <p>We confirm your address, hours and phone details across trusted directories, so search engines see one consistent record. Matching details build trust, lift your ranking and make it simple for a client to call, visit or send a message.</p>
    <p>Reviews from past clients add weight to every profile. We show ratings clearly beside your practice areas, helping new visitors choose with confidence and giving search engines fresh content that keeps your page moving up the list.</p>
    <h3>Sub Head</h3>
    <p>Good content answers real questions. Short guides on divorce, injury, estate planning and business law bring steady visits, and each guide links back to your profile so readers can reach your office the moment they are ready.</p>
  </div>
  <div class="column column--right">
    <p>Mobile visitors now make up most searches for lawyers. Every page adapts to phones and tablets, with large buttons that let clients call your office in one tap.</p>
    <h3>Sub Head</h3>
    <p>Clear monthly reports show exactly where each new enquiry came from.</p>
    <p>You will see visits, calls and emails in one simple summary. We compare results over time and suggest small changes that bring better leads, so your budget is always spent on the pages and terms that work best for your firm.</p>
    <p>Our support team is on hand to answer questions, update details and add new attorneys or practice areas whenever your firm grows.</p>
  </div>
  <p class="page-footer">Address: <b>2715 West Juniper Avenue, Suite 1400, Scottsdale, Arizona 85317</b> &nbsp; Email: <b>sales@brightcounselpages.com</b></p>
</section>

<section class="page page--r2 page--c2">
  <svg class="page-art" viewBox="0 0 353 353">
    <defs>
      <radialGradient id="art-globe" cx="0.55" cy="0.45" r="0.8">
        <stop offset="0" stop-color="#f2f6fb"/><stop offset="0.35" stop-color="#bcd2ea"/><stop offset="0.7" stop-color="#6f9ccd"/><stop offset="1" stop-color="#2b62a7"/>
      </radialGradient>
    </defs>
    <path d="M110 353 C140 250 250 170 353 150 L353 353 Z" fill="var(--swoosh)"/>
    <path d="M110 353 C140 250 250 170 353 150" fill="none" stroke="var(--swoosh-edge)" stroke-width="2"/>
    <path role="img" aria-label="Photo of a crystal globe resting on financial newspapers" fill="url(#art-globe)" d="M170 252 C170 207 228 187 284 189 C334 191 360 216 356 256 C352 288 338 302 322 308 L340 330 L300 312 C240 320 170 302 170 252 Z"/>
  </svg>
  <div class="page-band"></div>
  <h2 class="page-title">Maximise Your Online ROI</h2>
  <div class="column column--left">
    <h3>Sub Head</h3>
    <p>Every listing is written to be found by local clients searching for trusted legal help.</p>
    <p>Search engines reward pages that are clear, fast and useful. We build each firm profile with plain headings, accurate practice areas and local terms that match what people type, so your name appears where new clients begin their search for advice.</p>
    <p>Regular updates keep your profile fresh in the results. Our team reviews keywords, links and page speed each month, then reports the gains in simple terms so you always know how your listing performs against other firms nearby.</p>
    <h3>Sub Head</h3>
    <p>Strong local signals help your firm stand out in the map results for your city.</p>
    <p>We confirm your address, hours and phone details across trusted directories, so search engines see one consistent record. Matching details build trust, lift your ranking and make it simple for a client to call, visit or send a message.</p>
    <p>Reviews from past clients add weight to every profile. We show ratings clearly beside your practice areas, helping new visitors choose with confidence and giving search engines fresh content that keeps your page moving up the list.</p>
    <h3>Sub Head</h3>
    <p>Good content answers real questions. Short guides on divorce, injury, estate planning and business law bring steady visits, and each guide links back to your profile so readers can reach your office the moment they are ready.</p>
  </div>
  <div class="column column--right">
    <p>Mobile visitors now make up most searches for lawyers. Every page adapts to phones and tablets, with large buttons that let clients call your office in one tap.</p>
    <h3>Sub Head</h3>
    <p>Clear monthly reports show exactly where each new enquiry came from.</p>
    <p>You will see visits, calls and emails in one simple summary. We compare results over time and suggest small changes that bring better leads, so your budget is always spent on the pages and terms that work best for your firm.</p>
    <p>Our support team is on hand to answer questions, update details and add new attorneys or practice areas whenever your firm grows.</p>
  </div>
  <p class="page-footer">Address: <b>2715 West Juniper Avenue, Suite 1400, Scottsdale, Arizona 85317</b> &nbsp; Email: <b>sales@brightcounselpages.com</b></p>
</section>

<section class="page page--r2 page--c3">
  <svg class="page-art" viewBox="0 0 353 353">
    <defs>
      <radialGradient id="art-coins" cx="0.5" cy="0.4" r="0.85">
        <stop offset="0" stop-color="#d3e1ee"/><stop offset="0.35" stop-color="#8fadcb"/><stop offset="0.7" stop-color="#4c77a5"/><stop offset="1" stop-color="#1d4a80"/>
      </radialGradient>
    </defs>
    <path d="M110 353 C140 250 250 170 353 150 L353 353 Z" fill="var(--swoosh)"/>
    <path d="M110 353 C140 250 250 170 353 150" fill="none" stroke="var(--swoosh-edge)" stroke-width="2"/>
    <path role="img" aria-label="Photo of a pile of silver coins" fill="url(#art-coins)" d="M170 250 C170 205 228 185 284 187 C334 189 360 214 356 254 C352 286 338 302 322 308 L340 330 L300 312 C240 322 170 302 170 250 Z"/>
  </svg>
  <div class="page-band"></div>
  <h2 class="page-title">Pricing Plans</h2>
  <div class="column column--left">
    <h3>Sub Head</h3>
    <p>Every listing is written to be found by local clients searching for trusted legal help.</p>
    <p>Search engines reward pages that are clear, fast and useful. We build each firm profile with plain headings, accurate practice areas and local terms that match what people type, so your name appears where new clients begin their search for advice.</p>
    <p>Regular updates keep your profile fresh in the results. Our team reviews keywords, links and page speed each month, then reports the gains in simple terms so you always know how your listing performs against other firms nearby.</p>
    <h3>Sub Head</h3>
    <p>Strong local signals help your firm stand out in the map results for your city.</p>
    <p>We confirm your address, hours and phone details across trusted directories, so search engines see one consistent record. Matching details build trust, lift your ranking and make it simple for a client to call, visit or send a message.</p>
    <p>Reviews from past clients add weight to every profile. We show ratings clearly beside your practice areas, helping new visitors choose with confidence and giving search engines fresh content that keeps your page moving up the list.</p>
    <h3>Sub Head</h3>
    <p>Good content answers real questions. Short guides on divorce, injury, estate planning and business law bring steady visits, and each guide links back to your profile so readers can reach your office the moment they are ready.</p>
  </div>
  <div class="column column--right">
    <p>Mobile visitors now make up most searches for lawyers. Every page adapts to phones and tablets, with large buttons that let clients call your office in one tap.</p>
    <h3>Sub Head</h3>
    <p>Clear monthly reports show exactly where each new enquiry came from.</p>
    <p>You will see visits, calls and emails in one simple summary. We compare results over time and suggest small changes that bring better leads, so your budget is always spent on the pages and terms that work best for your firm.</p>
    <p>Our support team is on hand to answer questions, update details and add new attorneys or practice areas whenever your firm grows.</p>
  </div>
  <p class="page-footer">Address: <b>2715 West Juniper Avenue, Suite 1400, Scottsdale, Arizona 85317</b> &nbsp; Email: <b>sales@brightcounselpages.com</b></p>
</section>

</body>
</html>
```